Pedicure Menu with 8 Scent Options

This design will be for a single page menu (front/back) that will display multiple different scent variations of a product. The purpose of this menu is to display to clients and show them the available options and benefits of each option.
The menu will be double sided.
The front page will include a header including brand logo and product name, and a total of 8 different scents including imagery and descriptive text.
The design should include the text provided for each scent. The design should have a layout that is structured/organized, easy to read, and has bright imagery that represents each scent.
An example is a modular layout using boxes that highlight a different scent within each box. Lavender scent should include aesthetic images of lavender flower and/or the color purple.
The back page will include brand logo, overall product description, and additional brief text that explains each step of the product.
The final size of the design should be 8.5"x11", produced in InDesign format, with all layers editable for future changes.
NOTE: Please carefully review the attached design brief that includes additional information, and all necessary text to include in the design.
Target Market(s)
Beauty/Spa Clients
Industry/Entity Type
Beauty
Requirements
Must have
- Bright and Vivid Imagery/Illustrations
Nice to have
- Background design that utilizes, lines, shapes, or other elements.

```html
<!DOCTYPE html>
<html lang="en">
<head>
<meta charset="utf-8">
<title>Velora Deluxe Pedicure Menu</title>
<link href="https://fonts.googleapis.com/css2?family=Quicksand:wght@500;700&family=Open+Sans:wght@400&family=Yellowtail&display=swap" rel="stylesheet">
<style>
  :root {
    --stage: #2a2a2a;
    --purple-deep: #716d9f;
    --purple-mid: #8d88b6;
    --lavender: #b5a8d8;
    --teal: #a9d8d5;
    --teal-line: #9fd6d2;
    --white: #ffffff;
    --ink: #2f2f33;
    --mandarin: #e8772a;
    --leaf: #8ab83c;
    --rose: #e07a96;
    --honey: #dc9c46;
  }
  * { box-sizing: border-box; margin: 0; padding: 0; }
  html, body { width: 1200px; height: 1200px; overflow: hidden; }
  body { background: var(--stage); position: relative; font-family: "Open Sans", sans-serif; color: var(--ink); }

  .page { position: absolute; top: 250px; width: 540px; height: 699px; background: var(--white); overflow: hidden; }
  .page--front { left: 40px; }
  .page--back { left: 620px; }
  .page__art { position: absolute; inset: 0; width: 540px; height: 699px; }

  .brand { position: absolute; top: 28px; color: var(--white); font-family: "Quicksand", sans-serif; font-weight: 500; text-align: right; }
  .brand__name { font-size: 68px; line-height: 1; letter-spacing: 1px; display: block; }
  .brand__tag { font-size: 11px; letter-spacing: 3px; display: block; margin-top: 2px; }
  .page--front .brand { left: 82px; }
  .page--back .brand { left: 170px; }

  .title { position: absolute; font-family: "Quicksand", sans-serif; font-weight: 700; color: var(--white); white-space: nowrap; }
  .page--front .title { left: 32px; top: 118px; font-size: 33px; }
  .page--back .title { left: 0; width: 540px; text-align: center; top: 128px; font-size: 40px; }
  .steps-tag { position: absolute; left: 245px; top: 146px; font-family: "Yellowtail", cursive; font-size: 38px; line-height: 1.1; color: var(--purple-deep); transform: rotate(-6deg); }

  .pick { position: absolute; left: 74px; top: 226px; font-family: "Quicksand", sans-serif; font-weight: 700; line-height: 1; }
  .pick__small { display: block; font-size: 19px; color: var(--purple-deep); letter-spacing: 1px; }
  .pick__big { display: block; font-size: 33px; color: var(--lavender); margin-top: 3px; }

  .scent { position: absolute; width: 250px; height: 90px; }
  .scent__image { position: absolute; left: 0; top: 8px; width: 68px; height: 68px; border-radius: 50%; }
  .scent__name { position: absolute; left: 82px; top: 0; font-family: "Yellowtail", cursive; font-weight: 400; font-size: 19px; line-height: 1; }
  .scent__text { position: absolute; left: 82px; top: 23px; width: 146px; font-size: 7px; line-height: 1.35; text-align: justify; }

  .lead { position: absolute; left: 32px; top: 243px; font-family: "Quicksand", sans-serif; font-weight: 700; font-size: 21px; color: var(--purple-deep); letter-spacing: 1px; }
  .lead span { color: var(--lavender); }
  .intro { position: absolute; left: 32px; top: 284px; width: 490px; font-size: 10.6px; line-height: 1.4; }

  .step { position: absolute; width: 220px; height: 150px; text-align: center; }
  .step__circle { position: absolute; left: 70px; top: 0; width: 84px; height: 84px; border-radius: 50%; background: var(--teal); }
  .step__badge { position: absolute; left: 44px; top: 10px; width: 30px; height: 28px; }
  .step__name { position: absolute; left: 0; width: 220px; top: 90px; font-family: "Yellowtail", cursive; font-weight: 400; font-size: 28px; color: var(--lavender); line-height: 1; }
  .step__text { position: absolute; left: 0; width: 220px; top: 126px; font-size: 11.2px; }
</style>
</head>
<body>

<section class="page page--front">
  <svg class="page__art" viewBox="0 0 540 699">
    <defs>
      <linearGradient id="headFront" x1="0" y1="0" x2="1" y2="1">
        <stop offset="0" stop-color="#736fa2"/>
        <stop offset="0.55" stop-color="#a7b9cc"/>
        <stop offset="1" stop-color="#a9d8d5"/>
      </linearGradient>
      <linearGradient id="photoTone" x1="0" y1="0" x2="1" y2="1">
        <stop offset="0" stop-color="#d7cfdf" stop-opacity="0"/>
        <stop offset="0.35" stop-color="#eee6e2"/>
        <stop offset="1" stop-color="#f4ece6"/>
      </linearGradient>
      <linearGradient id="footFront" x1="0" y1="0" x2="1" y2="0">
        <stop offset="0" stop-color="#b9aed9"/>
        <stop offset="1" stop-color="#6e6a9e"/>
      </linearGradient>
    </defs>
    <rect width="540" height="300" fill="url(#headFront)"/>
    <g role="img" aria-label="Photo of bare feet with white pedicured toenails resting on soft white fur">
      <path d="M250,0 L540,0 L540,270 L250,270 C240,160 250,60 250,0Z" fill="url(#photoTone)"/>
      <ellipse cx="430" cy="130" rx="62" ry="90" fill="#e2b594" opacity="0.55"/>
    </g>
    <path d="M0,272 C20,264 36,244 38,222 C42,198 80,177 140,177 C230,177 330,256 440,260 C495,262 525,229 540,205 L540,699 L0,699Z" fill="#fff"/>
    <path d="M44,262 C44,205 80,183 140,183 C230,183 330,262 440,266 C495,268 525,235 540,212" fill="none" stroke="var(--lavender)" stroke-width="5"/>
    <path d="M0,699 L0,686 C140,658 330,698 480,680 C518,676 532,650 540,614 L540,699Z" fill="url(#footFront)"/>
    <path d="M0,678 C140,648 330,690 480,672 C518,668 530,644 536,612" fill="none" stroke="var(--teal-line)" stroke-width="6"/>
  </svg>

  <div class="brand"><span class="brand__name">Velora</span><span class="brand__tag">BEAUTY &amp; SPA</span></div>
  <h1 class="title">DELUXE PEDICURE</h1>
  <div class="steps-tag">4-Step</div>
  <div class="pick"><span class="pick__small">PICK YOUR</span><span class="pick__big">PEDICURE</span></div>

  <article class="scent" style="left:28px;top:290px">
    <div class="scent__image" role="img" aria-label="Lavender sprigs on a lilac circle" style="background:radial-gradient(circle,#c9bde6,#9f8fcc)"></div>
    <h2 class="scent__name" style="color:var(--lavender)">Lavender</h2>
    <p class="scent__text">Melt away the stresses of the day with a delicate, sweet smell that is floral and woodsy at the same time. Lavender is a calming scent for relaxation that puts us in a better mood and helps create a sense of tranquility and peacefulness.</p>
  </article>
  <article class="scent" style="left:22px;top:384px">
    <div class="scent__image" role="img" aria-label="Whole and peeled mandarin oranges" style="background:radial-gradient(circle,#f7a23c,#e8772a)"></div>
    <h2 class="scent__name" style="color:var(--mandarin)">Mandarin</h2>
    <p class="scent__text" style="left:88px">Uplift your senses with a fruity and sweet aroma that promotes clarity, radiance and a smooth, even skin tone. A citrus blend of essential oils works great to polish dull skin, reduce wrinkles, and correct spots.</p>
  </article>
  <article class="scent" style="left:28px;top:470px">
    <div class="scent__image" role="img" aria-label="White jasmine blossoms on a green circle" style="background:radial-gradient(circle,#f4f6ee 45%,#a8cc5a)"></div>
    <h2 class="scent__name" style="color:var(--leaf)">Jasmine</h2>
    <p class="scent__text">Embrace the warmth of a rich and sensual floral scent that boosts your energy levels and helps make your day better and brighter. A symbol of purity, love, and beauty – Jasmine helps to reduce exhaustion, nervousness, and stress.</p>
  </article>
  <article class="scent" style="left:22px;top:564px">
    <div class="scent__image" role="img" aria-label="Sliced cantaloupe melon and cucumber" style="background:radial-gradient(circle,#f4b36a,#7fb13a)"></div>
    <h2 class="scent__name" style="color:var(--leaf)">Cucumber-Melon</h2>
    <p class="scent__text" style="left:88px">Jump into a refreshing blend of crisp cucumber, watery honeydew, and summer cantaloupe. Perfect for capturing the essence of a summer day. Bamboo and aloe extract help cool your skin after a day in the sun.</p>
  </article>

  <article class="scent" style="left:283px;top:290px">
    <div class="scent__image" role="img" aria-label="Fresh mint leaves" style="background:radial-gradient(circle,#6fbf6a,#2f8f48)"></div>
    <h2 class="scent__name" style="color:var(--leaf)">Mint</h2>
    <p class="scent__text">Rejuvenate your body with a cool mix of peppermint and spearmint that prevents skin damage, alleviates inflamed skin, and acts as a splash of tonic for the senses. Infused with eucalyptus to leave you clean, cool, and crisp.</p>
  </article>
  <article class="scent" style="left:283px;top:381px">
    <div class="scent__image" role="img" aria-label="Pink roses on a soft pink circle" style="background:radial-gradient(circle,#f08aa8,#fbe1ea)"></div>
    <h2 class="scent__name" style="color:var(--rose)">Rose</h2>
    <p class="scent__text">Fall in love with a delicate floral twist of spicy and sweet that nourishes your skin and calms the mind. Essential oils help to reduce fine lines and protect the skin from UV damage.</p>
  </article>
  <article class="scent" style="left:283px;top:460px">
    <div class="scent__image" role="img" aria-label="Milk bottle and a jar of honey" style="background:radial-gradient(circle,#f7f3ea 35%,#e0a25c)"></div>
    <h2 class="scent__name" style="color:var(--honey)">Milk &amp; Honey</h2>
    <p class="scent__text">Discover one of nature's most luxurious skin cleansers and softeners. Creamy milk is full of rich essential vitamins that supply abundant moisture and improves skin elasticity. Sweet honey contains antioxidants and other nutrients that slow down skin aging.</p>
  </article>
  <article class="scent" style="left:283px;top:562px">
    <div class="scent__image" role="img" aria-label="Cup of green tea with tea leaves" style="background:radial-gradient(circle,#d9894a 25%,#c8d7b0)"></div>
    <h2 class="scent__name" style="color:var(--leaf)">Green Tea</h2>
    <p class="scent__text">Restore a sense of serenity with fragrant green tea extract that helps to relax the mind, reduces redness and swelling, and leaves the skin feeling hydrated, silky, and smooth. A natural detoxification that will supplies abundant moisture to the skin.</p>
  </article>
</section>

<section class="page page--back">
  <svg class="page__art" viewBox="0 0 540 699" aria-hidden="true">
    <defs>
      <linearGradient id="headBack" x1="0" y1="0" x2="1" y2="1">
        <stop offset="0" stop-color="#736fa2"/>
        <stop offset="0.5" stop-color="#a7b9cc"/>
        <stop offset="1" stop-color="#a9d8d5"/>
      </linearGradient>
      <linearGradient id="footBack" x1="0" y1="0" x2="1" y2="0">
        <stop offset="0" stop-color="#b9aed9"/>
        <stop offset="1" stop-color="#6e6a9e"/>
      </linearGradient>
    </defs>
    <rect width="540" height="300" fill="url(#headBack)"/>
    <path d="M0,272 C18,264 34,244 36,222 C40,196 70,177 112,177 C220,177 350,239 445,239 C500,239 528,216 540,193 L540,699 L0,699Z" fill="#fff"/>
    <path d="M43,262 C43,205 70,183 112,183 C220,183 350,245 445,245 C500,245 528,222 540,200" fill="none" stroke="var(--lavender)" stroke-width="5"/>
    <line x1="270" y1="330" x2="270" y2="464" stroke="var(--teal-line)" stroke-width="1.5"/>
    <line x1="270" y1="486" x2="270" y2="630" stroke="var(--teal-line)" stroke-width="1.5"/>
    <line x1="44" y1="482" x2="248" y2="482" stroke="var(--teal-line)" stroke-width="1.5"/>
    <line x1="292" y1="482" x2="496" y2="482" stroke="var(--teal-line)" stroke-width="1.5"/>
    <path d="M0,699 L0,686 C140,658 330,698 480,680 C518,676 532,650 540,614 L540,699Z" fill="url(#footBack)"/>
    <path d="M0,678 C140,648 330,690 480,672 C518,668 530,644 536,612" fill="none" stroke="var(--teal-line)" stroke-width="6"/>
  </svg>

  <div class="brand"><span class="brand__name">Velora</span><span class="brand__tag">BEAUTY &amp; SPA</span></div>
  <h1 class="title">DELUXE PEDICURE</h1>
  <h2 class="lead">4 ESSENTIAL <span>STEPS:</span></h2>
  <p class="intro">Velora Deluxe Pedicure 4-Step will transform your pedicure experience and immerse your senses into a floral paradise designed to rejuvenate your body. Sit back, relax, and enjoy.</p>

  <div class="step" style="left:34px;top:331px">
    <div class="step__circle"></div>
    <svg class="step__badge" viewBox="0 0 30 28"><path d="M15,27 C4,19 0,13 0,8 C0,3 4,0 8,0 C11,0 13,2 15,4 C17,2 19,0 22,0 C26,0 30,3 30,8 C30,13 26,19 15,27Z" fill="var(--purple-deep)"/><text x="15" y="16" text-anchor="middle" font-family="Quicksand, sans-serif" font-weight="700" font-size="11" fill="#fff">1</text></svg>
    <h3 class="step__name">Salt Soak</h3>
    <p class="step__text">Detoxifies and deodorizes your feet.</p>
  </div>
  <div class="step" style="left:282px;top:331px">
    <div class="step__circle"></div>
    <svg class="step__badge" viewBox="0 0 30 28"><path d="M15,27 C4,19 0,13 0,8 C0,3 4,0 8,0 C11,0 13,2 15,4 C17,2 19,0 22,0 C26,0 30,3 30,8 C30,13 26,19 15,27Z" fill="var(--purple-deep)"/><text x="15" y="16" text-anchor="middle" font-family="Quicksand, sans-serif" font-weight="700" font-size="11" fill="#fff">2</text></svg>
    <h3 class="step__name">Sugar Scrub</h3>
    <p class="step__text">Gently exfoliates dead skin.</p>
  </div>
  <div class="step" style="left:34px;top:502px">
    <div class="step__circle"></div>
    <svg class="step__badge" viewBox="0 0 30 28"><path d="M15,27 C4,19 0,13 0,8 C0,3 4,0 8,0 C11,0 13,2 15,4 C17,2 19,0 22,0 C26,0 30,3 30,8 C30,13 26,19 15,27Z" fill="var(--purple-deep)"/><text x="15" y="16" text-anchor="middle" font-family="Quicksand, sans-serif" font-weight="700" font-size="11" fill="#fff">3</text></svg>
    <h3 class="step__name">Foot Masque</h3>
    <p class="step__text">Cleanses pores for smoother skin.</p>
  </div>
  <div class="step" style="left:282px;top:502px">
    <div class="step__circle"></div>
    <svg class="step__badge" viewBox="0 0 30 28"><path d="M15,27 C4,19 0,13 0,8 C0,3 4,0 8,0 C11,0 13,2 15,4 C17,2 19,0 22,0 C26,0 30,3 30,8 C30,13 26,19 15,27Z" fill="var(--purple-deep)"/><text x="15" y="16" text-anchor="middle" font-family="Quicksand, sans-serif" font-weight="700" font-size="11" fill="#fff">4</text></svg>
    <h3 class="step__name">Massage Lotion</h3>
    <p class="step__text">Hydrates and soothes skin.</p>
  </div>
</section>

</body>
</html>
```